Upscale business cards needed for Board of Directors

We need professional business cards created for members of our family business Board of Directors. We would like these relatively simple and straightforward, but also with a unique element to set them apart. Probably stick with neutral and simple colors - white, grey etc. We need space for the traditional elements, including name, title, address, email/phone number. And we will be creating several from this template so it needs to be template that is easy to switch information in and out of.
Business
See description

```html
<!DOCTYPE html>
<html lang="en">
<head>
<meta charset="UTF-8">
<title>Braemoor Holdings – Business Card</title>
<link rel="stylesheet" href="https://fonts.googleapis.com/css2?family=Montserrat:wght@400;500;700&display=swap">
<style>
  :root {
    --bg: #ececec;
    --card-white: #ffffff;
    --gold: #a08b5e;
    --ink: #1b1b1b;
    --ink-soft: #4a4a4a;
    --rule: #cfcfcf;
  }
  * { margin: 0; padding: 0; box-sizing: border-box; }
  html, body {
    width: 1200px; height: 730px; overflow: hidden;
    background: var(--bg);
    font-family: "Montserrat", Arial, sans-serif;
  }
  .sheet {
    width: 1200px; height: 730px;
    display: flex; align-items: center; justify-content: center; gap: 60px;
  }
  .card {
    position: relative;
    width: 500px; height: 286px;
    box-shadow: 0 6px 18px rgba(0,0,0,0.12);
    overflow: hidden;
  }
  /* Front */
  .card--front { background: var(--card-white); color: var(--ink); }
  .holder { position: absolute; left: 40px; top: 66px; }
  .holder__name { font-size: 17px; font-weight: 700; letter-spacing: 0.5px; }
  .holder__title { font-size: 10px; font-weight: 500; color: var(--gold); margin-top: 3px; }
  .contacts {
    position: absolute; left: 40px; top: 170px; right: 40px;
    font-size: 10px; color: var(--ink-soft);
  }
  .contacts__row { display: flex; align-items: center; gap: 8px; margin-bottom: 8px; }
  .contacts__item { display: flex; align-items: center; gap: 5px; }
  .contacts__sep { width: 1px; height: 11px; background: var(--rule); }
  .icon { width: 11px; height: 11px; flex: none; }
  .icon path, .icon circle, .icon rect { stroke: var(--gold); fill: none; stroke-width: 1.4; }

  .brand {
    display: flex; align-items: center; gap: 8px;
    font-weight: 700; color: var(--ink); white-space: nowrap;
  }
  .brand__square { width: 10px; height: 10px; background: var(--ink); flex: none; }
  .card--front .brand { position: absolute; right: 40px; top: 78px; font-size: 19px; }

  .front-rule { position: absolute; left: 40px; right: 40px; top: 244px; height: 1px; background: var(--rule); }
  .band { position: absolute; bottom: 0; height: 7px; }
  .band--dark { left: 0; width: 290px; background: var(--ink); }
  .band--gold { left: 290px; right: 0; background: var(--gold); }

  /* Back */
  .card--back {
    background: var(--gold);
    display: flex; align-items: center; justify-content: center;
  }
  .card--back .brand { font-size: 28px; gap: 10px; }
  .card--back .brand__square { width: 14px; height: 14px; }
</style>
</head>
<body>
<main class="sheet">
  <section class="card card--front" aria-label="Card front">
    <div class="holder">
      <p class="holder__name">OLIVER GRANT</p>
      <p class="holder__title">Managing Director</p>
    </div>

    <div class="brand">
      <span class="brand__square"></span>
      <span class="brand__name">Braemoor Holdings</span>
    </div>

    <div class="contacts">
      <div class="contacts__row">
        <span class="contacts__item">
          <svg class="icon" viewBox="0 0 12 12"><path d="M3 1.5 L4.6 1.5 L5.4 4 L4.2 5 C4.8 6.4 5.6 7.2 7 7.8 L8 6.6 L10.5 7.4 L10.5 9 C10.5 9.8 9.8 10.5 9 10.5 C5 10.3 1.7 7 1.5 3 C1.5 2.2 2.2 1.5 3 1.5 Z"/></svg>
          (0044) 20 71588
        </span>
        <span class="contacts__sep"></span>
        <span class="contacts__item">
          <svg class="icon" viewBox="0 0 12 12"><rect x="1" y="2.5" width="10" height="7"/><path d="M1 2.5 L6 6.5 L11 2.5"/></svg>
          office@braemoor.co
        </span>
        <span class="contacts__sep"></span>
        <span class="contacts__item">
          <svg class="icon" viewBox="0 0 12 12"><circle cx="6" cy="6" r="4.8"/><path d="M1.2 6 H10.8 M6 1.2 C3.8 4 3.8 8 6 10.8 M6 1.2 C8.2 4 8.2 8 6 10.8"/></svg>
          www.braemoor.co
        </span>
      </div>
      <div class="contacts__row">
        <span class="contacts__item">
          <svg class="icon" viewBox="0 0 12 12"><path d="M6 11 C6 11 2.2 7 2.2 4.6 A3.8 3.8 0 0 1 9.8 4.6 C9.8 7 6 11 6 11 Z"/><circle cx="6" cy="4.6" r="1.3"/></svg>
          Braemoor House, 18 Quayside Row, Leith EH6 7BT
        </span>
      </div>
    </div>

    <div class="front-rule"></div>
    <div class="band band--dark"></div>
    <div class="band band--gold"></div>
  </section>

  <section class="card card--back" aria-label="Card back">
    <div class="brand">
      <span class="brand__square"></span>
      <span class="brand__name">Braemoor Holdings</span>
    </div>
  </section>
</main>
</body>
</html>
```